Brenvick Holdings LLC, new Business cards

I'm moving offices and need new cards. Plus I'm open to modifying the current design of my card. I will keep the logo but would like to explore other layouts and fonts for the design. I've included the current double sided card for reference. I Like the navy color and white. Might be open to grays or silver. Needs to be clean and elegant.

Target Market(s)

Investors, buyers & sellers of private equities and real estate.

Contact Information for Business Card

Brenvick Holdings
Dorian P.K. Halvers, Managing Principal
418 Ostrander Ave., Suite 612
Denver, CO 80319
M: 970-555-0147, O: 303-555-0192
Dorian@brenvickholdings.example
Brenvickholdings.example

Colors
0354a2
ffffff
c4c4c4

Requirements
Must have
• Business card details.
• Logo raised or embossed, it was designed after a wax seal. Current has raised ink.
Nice to have
• Space on card to write additional notes.

```html
<!DOCTYPE html>
<html lang="en">
<head>
<meta charset="utf-8">
<title>Brenvick Holdings – Business Cards</title>
<link rel="stylesheet" href="https://fonts.googleapis.com/css2?family=Open+Sans:wght@400;600;700&display=swap">
<style>
  :root {
    --backdrop: #e2e2e2;
    --card: #ffffff;
    --navy: #2d2a5f;
    --rule: #23245a;
    --ink: #1f1f24;
    --title-blue: #3d63a6;
    --card-shadow: rgba(0, 0, 0, 0.14);
  }
  * { box-sizing: border-box; margin: 0; padding: 0; }
  html, body {
    width: 1200px;
    height: 864px;
    overflow: hidden;
  }
  body {
    background: var(--backdrop);
    font-family: "Open Sans", sans-serif;
    color: var(--ink);
    position: relative;
  }
  .card {
    position: absolute;
    width: 520px;
    height: 297px;
    background: var(--card);
    box-shadow: 0 6px 18px var(--card-shadow);
  }
  .card--back  { left: 610px; top: 80px; }
  .card--front { left: 70px;  top: 480px; }

  .brand {
    position: absolute;
    left: 0; right: 0;
    display: flex;
    align-items: center;
    justify-content: center;
    gap: 10px;
    color: var(--navy);
    font-weight: 700;
    letter-spacing: 0.14em;
    text-transform: uppercase;
    white-space: nowrap;
  }
  .brand__dot {
    border-radius: 50%;
    background: var(--navy);
    flex: none;
  }
  .card--back .brand { top: 92px; font-size: 22px; }
  .card--back .brand__dot { width: 22px; height: 22px; }
  .card--front .brand { top: 34px; font-size: 15px; }
  .card--front .brand__dot { width: 15px; height: 15px; }

  .website-row {
    position: absolute;
    left: 48px; right: 48px;
    top: 196px;
    display: flex;
    align-items: center;
    gap: 14px;
  }
  .website-row .rule { flex: 1; height: 2px; background: var(--rule); }
  .website {
    font-size: 21px;
    color: var(--navy);
    white-space: nowrap;
  }

  .rule--name {
    position: absolute;
    left: 40px; top: 96px;
    width: 110px; height: 1.5px;
    background: var(--rule);
  }
  .rule--contact {
    position: absolute;
    right: 40px; top: 176px;
    width: 100px; height: 1.5px;
    background: var(--rule);
  }
  .identity {
    position: absolute;
    left: 0; right: 0; top: 84px;
    text-align: center;
  }
  .identity__name {
    font-size: 17px;
    font-weight: 700;
    color: var(--ink);
  }
  .identity__title {
    font-size: 13px;
    color: var(--title-blue);
    margin-top: 1px;
  }
  .contact {
    position: absolute;
    left: 0; right: 0; top: 140px;
    text-align: center;
    font-size: 12.5px;
    line-height: 1.55;
    font-style: normal;
  }
</style>
</head>
<body>

  <section class="card card--back" aria-label="Card back">
    <div class="brand"><span class="brand__dot"></span>Brenvick Holdings</div>
    <div class="website-row">
      <span class="rule"></span>
      <span class="website">Brenvickholdings.example</span>
      <span class="rule"></span>
    </div>
  </section>

  <section class="card card--front" aria-label="Card front">
    <div class="brand"><span class="brand__dot"></span>Brenvick Holdings</div>
    <span class="rule--name"></span>
    <div class="identity">
      <p class="identity__name">Dorian P.K. Halvers</p>
      <p class="identity__title">Managing Principal</p>
    </div>
    <span class="rule--contact"></span>
    <address class="contact">
      M: 970-555-0147<br>
      O: 303-555-0192<br>
      Dorian@brenvickholdings.example<br>
      418 Ostrander Ave., Suite 612 Denver, CO 80319
    </address>
  </section>

</body>
</html>
```